Need new label for my eczema cream. The Reef Mended My Eczema. PLS NOTHING LAME AND CLIP ART-ISH!

Think marrowind website meets eczema....our site is reefmendskin.com ill attach our current logo.

```html
<!DOCTYPE html>
<html lang="en">
<head>
<meta charset="utf-8">
<title>The Reef Mended My Eczema – Soothing Cream Label</title>
<link href="https://fonts.googleapis.com/css2?family=Montserrat:wght@400;500;600;800&display=swap" rel="stylesheet">
<style>
  :root {
    --page-bg: #f5f5f5;
    --label-sky: #bce3eb;
    --ink-navy: #2a1a6b;
    --foam-white: #ffffff;
    --icon-tint: #9fd0dc;
  }
  html, body {
    margin: 0;
    padding: 0;
    width: 857px;
    height: 1200px;
    overflow: hidden;
    background: var(--page-bg);
    font-family: "Montserrat", sans-serif;
  }
  .label {
    position: absolute;
    left: 48px;
    top: 430px;
    width: 760px;
    height: 341px;
    background: var(--label-sky);
    overflow: hidden;
    color: var(--ink-navy);
  }
  .foam-band {
    position: absolute;
    left: 0;
    top: 270px;
    width: 760px;
    height: 71px;
  }
  .ingredient {
    position: absolute;
    width: 140px;
    left: 93px;
    text-align: center;
  }
  .ingredient-icon {
    display: block;
    width: 36px;
    height: 36px;
    margin: 0 auto;
    border-radius: 8px;
    background: var(--icon-tint);
  }
  .ingredient-name {
    display: block;
    margin-top: 6px;
    font-size: 20px;
    font-weight: 500;
    line-height: 1;
  }
  .ingredient--sea-moss { top: 30px; }
  .ingredient--aloe { top: 138px; }
  .ingredient--oats { top: 241px; }
  .product-title {
    position: absolute;
    left: 260px;
    top: 50px;
    margin: 0;
    font-size: 55px;
    font-weight: 800;
    line-height: 57px;
    letter-spacing: -0.5px;
  }
  .product-title sup {
    font-size: 10px;
    font-weight: 600;
    vertical-align: top;
    position: relative;
    top: 4px;
  }
  .brand-mark {
    position: absolute;
    left: 562px;
    top: 59px;
    width: 114px;
    height: 114px;
    border: 2px solid var(--foam-white);
    border-radius: 50%;
    box-sizing: border-box;
  }
  .product-type {
    position: absolute;
    left: 262px;
    top: 236px;
    margin: 0;
    font-size: 22px;
    font-weight: 400;
    letter-spacing: 7.6px;
    line-height: 1;
  }
  .net-volume {
    position: absolute;
    left: 262px;
    top: 298px;
    margin: 0;
    font-size: 15px;
    font-weight: 600;
    line-height: 1;
  }
</style>
</head>
<body>
  <section class="label" aria-label="Soothing cream label, front side">
    <svg class="foam-band" viewBox="0 0 760 71" preserveAspectRatio="none" aria-hidden="true">
      <path fill="var(--foam-white)" d="M0 10 C 15 2 30 2 45 8 S 75 14 90 8 S 120 2 135 8 S 165 14 180 8 S 210 2 225 8 S 255 14 270 8 S 300 2 315 8 S 345 14 360 8 S 390 2 405 8 S 435 14 450 8 S 480 2 495 8 S 525 14 540 8 S 570 2 585 8 S 615 14 630 8 S 660 2 675 8 S 705 14 720 8 S 750 2 760 6 L 760 71 L 0 71 Z"/>
    </svg>

    <div class="ingredient ingredient--sea-moss">
      <span class="ingredient-icon" role="img" aria-label="Line icon of sea moss"></span>
      <span class="ingredient-name">Sea Moss</span>
    </div>
    <div class="ingredient ingredient--aloe">
      <span class="ingredient-icon" role="img" aria-label="Line icon of an aloe vera plant"></span>
      <span class="ingredient-name">Aloe Vera</span>
    </div>
    <div class="ingredient ingredient--oats">
      <span class="ingredient-icon" role="img" aria-label="Line icon of an oat sprout"></span>
      <span class="ingredient-name">Oats</span>
    </div>

    <div class="brand-mark" aria-hidden="true"></div>

    <h1 class="product-title">THE REEF<br>MENDED<br>MY ECZEMA<sup>™</sup></h1>
    <p class="product-type">SOOTHING CREAM</p>
    <p class="net-volume">4 fl oz / 118 ml</p>
  </section>
</body>
</html>
```